Construction company that specializes in roofing and siding

https://bayfieldroofworks.com/featured-projects/

https://www.quarrymeadowrenewalllc.com/#

https://www.tallpinehomecrafters.com/residential-siding-services/

Please model a website after these examples
I posted a doc that has some content to get you started. I will upload more content and photos as the site progresses.

Coded - Design and coding required

5+ page

```html
<!DOCTYPE html>
<html lang="en">
<head>
<meta charset="utf-8">
<title>Ridgeline Construction – Standing Seam Steel Roofing</title>
<link href="https://fonts.googleapis.com/css2?family=Poppins:wght@400;500;600;700;800&display=swap" rel="stylesheet">
<style>
:root{
  --navy:#35455a;
  --navy-deep:#2c3a4d;
  --sky:#d3e4f8;
  --sky-light:#e6f0fb;
  --ink:#111418;
  --white:#ffffff;
  --black:#000000;
  --muted:#b9c0c9;
  --accent-bar:#a9b7c8;
}
*{margin:0;padding:0;box-sizing:border-box}
html,body{width:697px;height:1200px;overflow:hidden}
body{font-family:'Poppins',sans-serif;color:var(--ink);background:var(--white);position:relative}
.abs{position:absolute}

/* header */
.hero{left:0;top:0;width:697px;height:267px;background:linear-gradient(100deg,var(--sky) 0%,var(--sky-light) 55%,#eef4fb 100%);overflow:hidden}
.hero-photo{left:312px;top:0;width:385px;height:267px;background:linear-gradient(160deg,rgba(230,240,250,0) 0%,rgba(220,232,246,.3) 30%,#3b4150 55%,#5b4332 80%,#2b2e35 100%);clip-path:polygon(55% 0,100% 0,100% 100%,0 100%,45% 30%)}
.logo{left:56px;top:24px;display:flex;align-items:center;gap:5px;font-weight:800;font-size:11px;letter-spacing:.5px;color:var(--ink);line-height:1}
.logo small{display:block;font-weight:500;font-size:5px;letter-spacing:1.4px;margin-top:1px}
.logo-mark{width:22px;height:22px;border-radius:50%;background:var(--ink)}
.nav-strip{left:190px;top:14px;width:507px;height:34px;background:rgba(236,243,251,.85);clip-path:polygon(4% 0,100% 0,100% 100%,4% 100%,0 50%)}
.nav{left:209px;top:14px;height:34px;display:flex;align-items:center;font-size:6.3px;font-weight:500;color:var(--ink)}
.nav span{position:absolute;white-space:nowrap}
.nav .active::after{content:"";position:absolute;left:2px;right:2px;top:17px;height:1px;background:var(--ink)}
.btn-contact{left:557px;top:18px;width:84px;height:26px;background:var(--navy);color:var(--white);font-size:6.5px;font-weight:700;display:flex;align-items:center;justify-content:center;outline:1px solid var(--navy);border:1px solid var(--white)}
.hero-kicker{left:55px;top:95px;font-size:10.5px;font-weight:600}
.hero-title{left:55px;top:107px;font-size:27px;font-weight:800;line-height:29px;letter-spacing:-.3px}
.hero-bar{left:132px;top:153px;width:130px;height:13px;background:var(--accent-bar)}
.hero-title .soft{color:var(--navy)}
.btn-schedule{left:55px;top:180px;width:84px;height:26px;background:var(--navy);color:var(--white);font-size:6.3px;font-weight:700;display:flex;align-items:center;justify-content:center;border:1px solid var(--white);outline:1px solid var(--navy)}

/* about block */
.about-photo{left:282px;top:320px;width:358px;height:252px;background:linear-gradient(120deg,#2d5d80 0%,#4f86a9 35%,#7aa7c0 55%,#b8b86a 80%,#a7a7a0 100%)}
.about-frame{left:286px;top:324px;width:350px;height:244px;border:.6px solid rgba(255,255,255,.85)}
.about-card{left:91px;top:373px;width:268px;height:175px;background:var(--navy);color:var(--white);padding:32px 18px 0 21px;font-size:7.1px;line-height:10px}
.about-card p+p{margin-top:10px}

/* request section */
.request{left:0;top:629px;width:697px;height:356px;background:linear-gradient(180deg,#d9dde0 0%,#b9c0c5 55%,#4a4d52 80%,#35373b 100%)}
.form-outer{left:437px;top:674px;width:197px;height:267px;border:.7px solid var(--navy)}
.form-card{left:444px;top:683px;width:183px;height:251px;background:var(--navy)}
.form-title{left:444px;top:692px;width:183px;text-align:center;color:var(--white);font-weight:800;font-size:20px;letter-spacing:-.2px}
.field{left:461px;width:150px;height:26px;background:var(--white);font-size:6px;color:#8a8f96;padding:10px 10px 0}
.form-btn{left:461px;top:894px;width:150px;height:26px;background:var(--white);display:flex;align-items:center;justify-content:center;font-size:6.5px;font-weight:600;color:var(--navy)}
.form-btn::after{content:"";position:absolute;inset:2px;border:.7px solid var(--navy)}

/* footer */
.footer{left:0;top:985px;width:697px;height:215px;background:var(--black);color:var(--white)}
.map{left:444px;top:985px;width:253px;height:170px;background:linear-gradient(135deg,#e9eef2 0%,#cfe6ef 40%,#f1f3f5 65%,#bfe3ef 100%)}
.f-logo{left:53px;top:1020px;display:flex;align-items:center;gap:6px;font-weight:800;font-size:12px;color:var(--white);line-height:1;letter-spacing:.5px}
.f-logo small{display:block;font-weight:500;font-size:5.5px;letter-spacing:1.5px;margin-top:1px}
.f-logo .logo-mark{background:var(--white);width:28px;height:28px}
.social{top:1068px;width:23px;height:23px;border:.7px solid #3a3a3a;display:flex;align-items:center;justify-content:center}
.social i{width:6px;height:6px;background:var(--white);border-radius:50%}
.f-head{top:1028px;font-size:7.6px;font-weight:700}
.f-links{left:218px;top:1044px;font-size:6.6px;line-height:11px;list-style:none}
.f-links li::before{content:"»";margin-right:3px}
.contact-item{left:316px;font-size:6.8px;line-height:8px;padding-left:13px}
.contact-item svg{position:absolute;left:0;top:1px}
.contact-item .lbl{font-size:5.6px;color:var(--muted)}
.contact-item b{font-weight:600;letter-spacing:.3px}
.bottom-line{left:0;top:1155px;width:697px;height:.5px;background:#1e1e1e}
.copy{left:55px;top:1174px;font-size:6.3px;color:#d6d6d6}
.copy b{color:var(--white);font-weight:600}
.legal{left:516px;top:1174px;font-size:6.3px;color:#d6d6d6;display:flex;gap:12px}
</style>
</head>
<body>

<section class="abs hero">
  <div class="abs hero-photo" role="img" aria-label="Roofer hammering on a dark standing seam steel roof against a pale sky"></div>
</section>
<div class="abs nav-strip"></div>
<div class="abs logo"><span class="logo-mark"></span><span>RIDGELINE<small>CONSTRUCTION</small></span></div>
<nav class="abs nav">
  <span style="left:0">Home</span>
  <span style="left:33px">About</span>
  <span class="active" style="left:67px">Roofing ⌄</span>
  <span style="left:116px">Siding ⌄</span>
  <span style="left:156px">Gutters</span>
  <span style="left:199px">Windows</span>
  <span style="left:246px">Repair ⌄</span>
  <span style="left:285px">Storm Damage ⌄</span>
</nav>
<div class="abs btn-contact">CONTACT US</div>

<div class="abs hero-kicker">ROOFING</div>
<div class="abs hero-bar"></div>
<h1 class="abs hero-title">STANDING SEAM<br>STEEL <span class="soft">ROOFING</span></h1>
<div class="abs btn-schedule">SCHEDULE NOW</div>

<div class="abs about-photo" role="img" aria-label="Roofer in a hard hat and safety vest installing metal roof panels"></div>
<div class="abs about-frame"></div>
<div class="abs about-card">
  <p>Standing seam steel roofing is durable and long lasting. For homes and businesses, it is considered a premium upgrade over architectural shingles. While an architectural shingle roof in MN should typically be replaced after 20 years, a standing seam steel roof will not need replacement for at least 40 years making it the clear winner when it comes to durability.</p>
  <p>Already have an insurance claim for your architectural shingle roof? Ridgeline Construction can help you utilize your insurance claim to upgrade to a standing seam steel roof.</p>
</div>

<section class="abs request" role="img" aria-label="Two roofers fitting a vent pipe on a shingled roof under a cloudy sky"></section>
<div class="abs form-outer"></div>
<div class="abs form-card"></div>
<h2 class="abs form-title">REQUSET INFO</h2>
<div class="abs field" style="top:725px">Full Name</div>
<div class="abs field" style="top:757px">Email</div>
<div class="abs field" style="top:790px">Phone Number</div>
<div class="abs field" style="top:823px;height:57px">Full Name</div>
<div class="abs form-btn">SCHEDULE NOW</div>

<footer class="abs footer"></footer>
<div class="abs map" role="img" aria-label="Street map showing lakes and the company location pin"></div>
<div class="abs f-logo"><span class="logo-mark"></span><span>RIDGELINE<small>CONSTRUCTION</small></span></div>
<div class="abs social" style="left:53px" aria-label="Social link 1"><i></i></div>
<div class="abs social" style="left:80px" aria-label="Social link 2"><i></i></div>
<div class="abs social" style="left:107px" aria-label="Social link 3"><i></i></div>
<div class="abs social" style="left:134px" aria-label="Social link 4"><i></i></div>

<div class="abs f-head" style="left:218px;color:#fff">NANIGATION</div>
<ul class="abs f-links" style="color:#fff">
  <li>Roofing</li><li>Siding</li><li>Gutters</li><li>Windows</li><li>Repair</li><li>Storm Damage</li>
</ul>

<div class="abs f-head" style="left:316px;color:#fff">CONTACT INFO</div>
<div class="abs contact-item" style="top:1048px;color:#fff">
  <svg width="8" height="10" viewBox="0 0 8 10"><path d="M4 0a4 4 0 0 0-4 4c0 3 4 6 4 6s4-3 4-6a4 4 0 0 0-4-4zm0 5.5A1.5 1.5 0 1 1 4 2.5a1.5 1.5 0 0 1 0 3z" fill="#b9c0c9"/></svg>
  Address line come here,<br>Lorem ipsum, 123 456.
</div>
<div class="abs contact-item" style="top:1073px;color:#fff">
  <svg width="8" height="8" viewBox="0 0 8 8"><path d="M1.6 0 3 1.8 2.2 3a4.5 4.5 0 0 0 2.8 2.8L6.2 5 8 6.4 7 8C3 8 0 5 0 1z" fill="#b9c0c9"/></svg>
  <span class="lbl">Phone:</span><br><b>+123 456 7890</b>
</div>
<div class="abs contact-item" style="top:1099px;color:#fff">
  <svg width="9" height="7" viewBox="0 0 9 7"><rect width="9" height="7" fill="#b9c0c9"/><path d="M0 0l4.5 3.8L9 0" stroke="#000" stroke-width=".8" fill="none"/></svg>
  <span class="lbl">Email:</span><br>info@ridgelinemail.com
</div>

<div class="abs bottom-line"></div>
<div class="abs copy">Copyright © 2024 <b>Ridgeline</b> | All rights reserved.</div>
<div class="abs legal"><span>Privacy Policy</span><span>|</span><span>Terms of Conditins</span></div>

</body>
</html>
```